Etiketten für Nahrungsergänzung für Tiere
Zielgruppe
Wir stellen kolloidale Mischungen für Tiere her. Dies sind grob gesagt Nahrungsmittelergänzungen. Die Zielgruppe sind Tierbesitzer bzw. gesundheitsbewusste Menschen.
Aufgabenstellung
natürlich, in braun, beige, gold oder hellblau Tönen. Das Etikett wird auf eine Flasche aufgebraucht in der sich eine Flüssigkeit befindet. Das Etikett ist breiter als hoch. 115 x 61 mm (B x H)
Bisher haben wir blaue Flaschen verwendet und waren dadurch mit der Farbgebung ehr kühl und reduziert. In Zukunft wollen wir braune Flaschen mit schwarzen Deckel verwendet. Damit darf die Farbgebung auch wärmer, natürlich und das Etikett auch mit mehr Details versehen werden.
In den Uploads füge ich das aktuell Logo hinzu. Dies verwenden wir in braun/gold und in grün. Falls sich diese Gestaltung nicht so günstig auswirkt, haben wir ein 'alternative' Logo hinzugefügt. Da die Seite nächstes Jahr komplett überarbeitet wird und unsere Firma sich vergrößert, kann diese Änderung durchgeführt werden.
Ich lade noch ein Etikett hoch, welches wir für die Einzelelemente nutzen. Hier sind und bleiben die Flaschen nach wir vor blau (Herstellervorgaben), dadurch sind die Etikett sehr kühl und reduziert. Das darf auf den Entwurf für die Mischungen sehr gern deutlich verändert werden :-)

```html
<!DOCTYPE html>
<html lang="de">
<head>
<meta charset="utf-8">
<title>Feldquelle – Etikett Kolloidale Mischung, Veredelungsvarianten</title>
<link rel="stylesheet" href="https://fonts.googleapis.com/css2?family=PT+Sans:wght@400;700&family=Roboto+Slab:wght@400;500&family=PT+Sans+Narrow:wght@400;700&display=swap">
<style>
  :root{
    --page:#ffffff;
    --ink:#1d1d1b;
    --label-cream:#f3ece0;
    --label-text:#4a4036;
    --brand-brown:#5a4632;
    --wave-blue:#bcdcf0;
    --wave-blue-deep:#9fcbe8;
    --leaf-green:#dde7e0;
    --leaf-green-deep:#c4d5cb;
    --matte-gold:#c9a877;
    --aluminium:#b9bdc2;
    --copper:#c27a4f;
    --gold:#d8ae3e;
  }
  *{box-sizing:border-box;margin:0;padding:0}
  html,body{width:1200px;height:2257px;overflow:hidden;background:var(--page)}
  body{position:relative;font-family:"PT Sans",sans-serif;color:var(--ink)}

  .intro{position:absolute;left:98px;top:88px;width:1010px;font-size:27.5px;line-height:36px}

  .variant{position:absolute;width:545px;text-align:center}
  .variant .caption{font-size:29px;margin-top:46px}
  .col-left{left:45px}
  .col-right{left:600px}
  .row-1{top:390px}.row-2{top:870px}.row-3{top:1360px}.row-4{top:1850px}

  .label{position:relative;width:440px;height:234px;margin:0 auto;background:var(--label-cream);
    border-top:4px solid var(--foil);border-bottom:4px solid var(--foil);overflow:hidden;text-align:left;
    box-shadow:0 10px 24px rgba(0,0,0,.12)}
  .foil-matte{--foil:var(--matte-gold)}
  .foil-aluminium{--foil:var(--aluminium)}
  .foil-copper{--foil:var(--copper)}
  .foil-gold{--foil:var(--gold)}

  .panel{position:absolute;top:0;height:150px}
  .panel-left{left:0;width:135px;padding:46px 10px 0 14px}
  .panel-center{left:135px;width:170px;text-align:center;padding-top:10px;
    border-left:1px solid rgba(0,0,0,.05);border-right:1px solid rgba(0,0,0,.05)}
  .panel-right{left:305px;width:135px;padding:16px 8px 0 10px;font-family:"PT Sans Narrow",sans-serif;
    font-size:7.2px;line-height:8.8px;color:var(--label-text)}
  .panel-right b{display:block;margin-top:5px}

  .address-box{background:rgba(201,168,119,.35);font-size:7px;line-height:8.5px;padding:5px 4px;text-align:center;
    color:var(--label-text);margin-bottom:8px}
  .batch{font-family:"PT Sans Narrow",sans-serif;font-size:7px;line-height:8.5px;color:var(--label-text)}

  .mark-art{position:absolute;left:18px;top:30px;width:130px;height:100px;border-radius:40%;
    background:radial-gradient(ellipse at center,rgba(201,168,119,.18),rgba(201,168,119,0) 70%)}
  .brand-dot{position:relative;display:inline-block;width:26px;height:26px;border-radius:50%;border:2px solid var(--foil)}
  .brand{position:relative;font-size:10px;font-weight:700;letter-spacing:.5px;color:var(--brand-brown);margin-top:6px}
  .title{position:relative;font-family:"Roboto Slab",serif;font-weight:500;font-size:27px;line-height:30px;color:var(--brand-brown);margin-top:4px}
  .sub{position:relative;font-family:"Roboto Slab",serif;font-size:19px;line-height:22px;color:var(--brand-brown)}

  .band{position:absolute;left:0;top:160px;width:100%;height:36px}
  .band-wave{background:linear-gradient(180deg,var(--wave-blue),var(--wave-blue-deep))}
  .band-leaf{background:linear-gradient(180deg,var(--leaf-green),var(--leaf-green-deep))}
  .rule{position:absolute;left:0;width:100%;height:2px;background:var(--foil)}
  .rule-top{top:154px}.rule-bottom{top:202px}.rule-base{top:222px}
  .tag{position:absolute;left:187px;top:151px;width:66px;height:17px;border-radius:9px;background:var(--label-cream);
    border:1.5px solid var(--foil);font-family:"Roboto Slab",serif;font-size:9.5px;line-height:14px;text-align:center;color:var(--brand-brown)}
  .volume{position:absolute;left:135px;width:170px;top:206px;text-align:center;font-family:"Roboto Slab",serif;font-size:9.5px;color:var(--brand-brown)}
</style>
</head>
<body>
<p class="intro">Foiling ist eine hochwertige Veredelung, bei der eine glänzende Metallfolie (z. B. Gold, Silber) auf bestimmte Bereiche Ihres Designs aufgetragen wird, um einen eleganten und luxuriösen Effekt zu erzielen.</p>

<!-- Reihe 1 -->
<section class="variant col-left row-1">
  <div class="label foil-matte">
    <div class="panel panel-left"><div class="address-box">Feldquelle<br>Am Lindenhang 4<br>12345 Musterdorf</div><p class="batch"><b>MHD=Chargen-NR:</b><br>XXXXXXXXXXXXX</p></div>
    <div class="panel panel-center"><div class="mark-art" role="img" aria-label="Zarte Tierillustration mit Pferd und Katze"></div><span class="brand-dot"></span><p class="brand">FELDQUELLE</p><p class="title">Kolloidale</p><p class="sub">Mischung</p></div>
    <div class="panel panel-right">Bei Raumtemperatur und lichtgeschützt lagern. Vor Mikrowellen und magnetischen Feldern fernhalten.<b>PPM-Messmethode:</b>Atomspektralanalyse. Anwendung nach dem Quantenprinzip der verschränkten Teilchen. Nicht für den menschlichen Verzehr geeignet.</div>
    <div class="band band-wave" role="img" aria-label="Hellblaues Wellenmuster"></div>
    <span class="rule rule-top"></span><span class="rule rule-bottom"></span><span class="rule rule-base"></span>
    <span class="tag">Für Tiere</span><p class="volume">100ml</p>
  </div>
  <p class="caption">matte Goldfarbe</p>
</section>

<section class="variant col-right row-1">
  <div class="label foil-aluminium">
    <div class="panel panel-left"><div class="address-box">Feldquelle<br>Am Lindenhang 4<br>12345 Musterdorf</div><p class="batch"><b>MHD=Chargen-NR:</b><br>XXXXXXXXXXXXX</p></div>
    <div class="panel panel-center"><div class="mark-art" role="img" aria-label="Zarte Tierillustration mit Pferd und Katze"></div><span class="brand-dot"></span><p class="brand">FELDQUELLE</p><p class="title">Kolloidale</p><p class="sub">Mischung</p></div>
    <div class="panel panel-right">Bei Raumtemperatur und lichtgeschützt lagern. Vor Mikrowellen und magnetischen Feldern fernhalten.<b>PPM-Messmethode:</b>Atomspektralanalyse. Anwendung nach dem Quantenprinzip der verschränkten Teilchen. Nicht für den menschlichen Verzehr geeignet.</div>
    <div class="band band-wave" role="img" aria-label="Hellblaues Wellenmuster"></div>
    <span class="rule rule-top"></span><span class="rule rule-bottom"></span><span class="rule rule-base"></span>
    <span class="tag">Für Tiere</span><p class="volume">100ml</p>
  </div>
  <p class="caption">Aluminium-Folierung</p>
</section>

<!-- Reihe 2 -->
<section class="variant col-left row-2">
  <div class="label foil-copper">
    <div class="panel panel-left"><div class="address-box">Feldquelle<br>Am Lindenhang 4<br>12345 Musterdorf</div><p class="batch"><b>MHD=Chargen-NR:</b><br>XXXXXXXXXXXXX</p></div>
    <div class="panel panel-center"><div class="mark-art" role="img" aria-label="Zarte Tierillustration mit Pferd und Katze"></div><span class="brand-dot"></span><p class="brand">FELDQUELLE</p><p class="title">Kolloidale</p><p class="sub">Mischung</p></div>
    <div class="panel panel-right">Bei Raumtemperatur und lichtgeschützt lagern. Vor Mikrowellen und magnetischen Feldern fernhalten.<b>PPM-Messmethode:</b>Atomspektralanalyse. Anwendung nach dem Quantenprinzip der verschränkten Teilchen. Nicht für den menschlichen Verzehr geeignet.</div>
    <div class="band band-wave" role="img" aria-label="Hellblaues Wellenmuster"></div>
    <span class="rule rule-top"></span><span class="rule rule-bottom"></span><span class="rule rule-base"></span>
    <span class="tag">Für Tiere</span><p class="volume">100ml</p>
  </div>
  <p class="caption">Kupfer-Folierung</p>
</section>

<section class="variant col-right row-2">
  <div class="label foil-gold">
    <div class="panel panel-left"><div class="address-box">Feldquelle<br>Am Lindenhang 4<br>12345 Musterdorf</div><p class="batch"><b>MHD=Chargen-NR:</b><br>XXXXXXXXXXXXX</p></div>
    <div class="panel panel-center"><div class="mark-art" role="img" aria-label="Zarte Tierillustration mit Pferd und Katze"></div><span class="brand-dot"></span><p class="brand">FELDQUELLE</p><p class="title">Kolloidale</p><p class="sub">Mischung</p></div>
    <div class="panel panel-right">Bei Raumtemperatur und lichtgeschützt lagern. Vor Mikrowellen und magnetischen Feldern fernhalten.<b>PPM-Messmethode:</b>Atomspektralanalyse. Anwendung nach dem Quantenprinzip der verschränkten Teilchen. Nicht für den menschlichen Verzehr geeignet.</div>
    <div class="band band-wave" role="img" aria-label="Hellblaues Wellenmuster"></div>
    <span class="rule rule-top"></span><span class="rule rule-bottom"></span><span class="rule rule-base"></span>
    <span class="tag">Für Tiere</span><p class="volume">100ml</p>
  </div>
  <p class="caption">Gold-Folierung</p>
</section>

<!-- Reihe 3 -->
<section class="variant col-left row-3">
  <div class="label foil-matte">
    <div class="panel panel-left"><div class="address-box">Feldquelle<br>Am Lindenhang 4<br>12345 Musterdorf</div><p class="batch"><b>MHD=Chargen-NR:</b><br>XXXXXXXXXXXXX</p></div>
    <div class="panel panel-center"><div class="mark-art" role="img" aria-label="Zarte Tierillustration mit Pferd und Katze"></div><span class="brand-dot"></span><p class="brand">FELDQUELLE</p><p class="title">Kolloidale</p><p class="sub">Mischung</p></div>
    <div class="panel panel-right">Bei Raumtemperatur und lichtgeschützt lagern. Vor Mikrowellen und magnetischen Feldern fernhalten.<b>PPM-Messmethode:</b>Atomspektralanalyse. Anwendung nach dem Quantenprinzip der verschränkten Teilchen. Nicht für den menschlichen Verzehr geeignet.</div>
    <div class="band band-leaf" role="img" aria-label="Blattmuster in zartem Salbeigrün"></div>
    <span class="rule rule-top"></span><span class="rule rule-bottom"></span><span class="rule rule-base"></span>
    <span class="tag">Für Tiere</span><p class="volume">100ml</p>
  </div>
  <p class="caption">matte Goldfarbe</p>
</section>

<section class="variant col-right row-3">
  <div class="label foil-aluminium">
    <div class="panel panel-left"><div class="address-box">Feldquelle<br>Am Lindenhang 4<br>12345 Musterdorf</div><p class="batch"><b>MHD=Chargen-NR:</b><br>XXXXXXXXXXXXX</p></div>
    <div class="panel panel-center"><div class="mark-art" role="img" aria-label="Zarte Tierillustration mit Pferd und Katze"></div><span class="brand-dot"></span><p class="brand">FELDQUELLE</p><p class="title">Kolloidale</p><p class="sub">Mischung</p></div>
    <div class="panel panel-right">Bei Raumtemperatur und lichtgeschützt lagern. Vor Mikrowellen und magnetischen Feldern fernhalten.<b>PPM-Messmethode:</b>Atomspektralanalyse. Anwendung nach dem Quantenprinzip der verschränkten Teilchen. Nicht für den menschlichen Verzehr geeignet.</div>
    <div class="band band-leaf" role="img" aria-label="Blattmuster in zartem Salbeigrün"></div>
    <span class="rule rule-top"></span><span class="rule rule-bottom"></span><span class="rule rule-base"></span>
    <span class="tag">Für Tiere</span><p class="volume">100ml</p>
  </div>
  <p class="caption">Aluminium-Folierung</p>
</section>

<!-- Reihe 4 -->
<section class="variant col-left row-4">
  <div class="label foil-copper">
    <div class="panel panel-left"><div class="address-box">Feldquelle<br>Am Lindenhang 4<br>12345 Musterdorf</div><p class="batch"><b>MHD=Chargen-NR:</b><br>XXXXXXXXXXXXX</p></div>
    <div class="panel panel-center"><div class="mark-art" role="img" aria-label="Zarte Tierillustration mit Pferd und Katze"></div><span class="brand-dot"></span><p class="brand">FELDQUELLE</p><p class="title">Kolloidale</p><p class="sub">Mischung</p></div>
    <div class="panel panel-right">Bei Raumtemperatur und lichtgeschützt lagern. Vor Mikrowellen und magnetischen Feldern fernhalten.<b>PPM-Messmethode:</b>Atomspektralanalyse. Anwendung nach dem Quantenprinzip der verschränkten Teilchen. Nicht für den menschlichen Verzehr geeignet.</div>
    <div class="band band-leaf" role="img" aria-label="Blattmuster in zartem Salbeigrün"></div>
    <span class="rule rule-top"></span><span class="rule rule-bottom"></span><span class="rule rule-base"></span>
    <span class="tag">Für Tiere</span><p class="volume">100ml</p>
  </div>
  <p class="caption">Kupfer-Folierung</p>
</section>

<section class="variant col-right row-4">
  <div class="label foil-gold">
    <div class="panel panel-left"><div class="address-box">Feldquelle<br>Am Lindenhang 4<br>12345 Musterdorf</div><p class="batch"><b>MHD=Chargen-NR:</b><br>XXXXXXXXXXXXX</p></div>
    <div class="panel panel-center"><div class="mark-art" role="img" aria-label="Zarte Tierillustration mit Pferd und Katze"></div><span class="brand-dot"></span><p class="brand">FELDQUELLE</p><p class="title">Kolloidale</p><p class="sub">Mischung</p></div>
    <div class="panel panel-right">Bei Raumtemperatur und lichtgeschützt lagern. Vor Mikrowellen und magnetischen Feldern fernhalten.<b>PPM-Messmethode:</b>Atomspektralanalyse. Anwendung nach dem Quantenprinzip der verschränkten Teilchen. Nicht für den menschlichen Verzehr geeignet.</div>
    <div class="band band-leaf" role="img" aria-label="Blattmuster in zartem Salbeigrün"></div>
    <span class="rule rule-top"></span><span class="rule rule-bottom"></span><span class="rule rule-base"></span>
    <span class="tag">Für Tiere</span><p class="volume">100ml</p>
  </div>
  <p class="caption">Gold-Folierung</p>
</section>
</body>
</html>
```